businesscard, flyer and membercard

--------------------------------------------------------------------------------------------------
design flyer :
- delivering format (jpg, pdf and original psd)
- there is a example how the flyers should look like
the text and logo should be the same as the exemple flyer, the creativity is yours.
- the design should have a back and front side.
File format : 15,0 cm x 21,2 cm
design membercard :
- there is example how the member-card should look like
the text and logo should be the same as the exemple membercard, the creativity is yours.
- the front side contains text and open space where for writing :
Naam ......
Dansstijlen ......
- the front side contains 12 circels horizontal at the line name at the end of the line "Salsa".
- the front side contains 12 circels horizontal at the line name at the end of the line "Bachata".
- the front side contains 12 circels horizontal at the line name at the end of the line "Kizomba".
- each horizontal line with circels contains a different kind of color/design.
- file format: 7,6 cm x 10,7 cm
Business card :
- there is example how the businesscard should look like
the text and logo should be the same as the exemple buisinesscard, the creativity is yours.
- the design should have a back a front side
File format : 8,7 cm x 5,7 cm

Target Market(s)

Dancing :Salsa, Bachata and Kizomba

Colors

Designer to choose colors to be used in the design.

Requirements
Must have
• same text as seen on the examples.
Nice to have
• see the examples as attachments
Should not have
• - REMOVE TEXT "KOV" from the design
• - REMOVE TEXT "Gratis Parkeren"

```html
<!DOCTYPE html>
<html lang="nl">
<head>
<meta charset="utf-8">
<title>Solara Dance Studio – Lid Kaart</title>
<link href="https://fonts.googleapis.com/css2?family=Share+Tech+Mono&family=PT+Sans+Narrow:wght@700&family=Archivo:wght@800&display=swap" rel="stylesheet">
<style>
  :root {
    --bg-light: #f7f7f7;
    --bg-mid: #dcdcdc;
    --ink: #111111;
    --accent-red: #ee1111;
    --salsa: #47ffff;
    --bachata: #ff4dff;
    --kizomba: #8ea09e;
    --dot-stroke: #7a7a7a;
    --photo-dark: #2a2a2e;
    --photo-warm: #b88c70;
  }
  html, body {
    margin: 0;
    padding: 0;
    overflow: hidden;
    background: #ffffff;
  }
  .member-card {
    position: relative;
    width: 1200px;
    height: 853px;
    overflow: hidden;
    background:
      radial-gradient(ellipse at 55% 40%, rgba(255,255,255,0.95) 0%, rgba(255,255,255,0) 60%),
      linear-gradient(160deg, var(--bg-mid) 0%, var(--bg-light) 45%, var(--bg-mid) 100%);
  }
  .brand-name,
  .brand-sub {
    position: absolute;
    left: 90px;
    width: 310px;
    text-align: center;
    font-family: "Archivo", sans-serif;
    font-weight: 800;
    line-height: 1;
    color: var(--ink);
    white-space: nowrap;
  }
  .brand-name {
    top: 92px;
    font-size: 58px;
    letter-spacing: 4px;
  }
  .brand-sub {
    top: 234px;
    font-size: 27px;
  }
  .card-title {
    position: absolute;
    left: 448px;
    top: 121px;
    margin: 0;
    font-family: "Share Tech Mono", monospace;
    font-weight: 400;
    font-size: 96px;
    line-height: 1;
    letter-spacing: 4px;
    color: var(--accent-red);
    text-shadow: 2px 2px 3px rgba(0,0,0,0.25);
    white-space: nowrap;
  }
  .field {
    position: absolute;
    left: 85px;
    margin: 0;
    font-family: "Share Tech Mono", monospace;
    font-size: 50px;
    line-height: 1;
    letter-spacing: 1.6px;
    color: var(--accent-red);
    white-space: nowrap;
  }
  .field-name { top: 319px; }
  .field-styles { top: 390px; }
  .dancers-photo {
    position: absolute;
    left: 845px;
    top: 76px;
    width: 327px;
    height: 389px;
    clip-path: polygon(125px 0, 327px 0, 327px 389px, 40px 389px, 0 365px, 55px 190px, 120px 135px);
    background: radial-gradient(ellipse at 65% 35%, var(--photo-warm) 0%, var(--photo-dark) 55%, rgba(42,42,46,0.2) 100%);
  }
  .stamp-grid {
    position: absolute;
    left: 0;
    top: 0;
  }
  .style-label {
    position: absolute;
    left: 979px;
    font-family: "PT Sans Narrow", sans-serif;
    font-weight: 700;
    font-size: 45px;
    line-height: 1;
    color: var(--accent-red);
    text-shadow: 2px 2px 2px rgba(0,0,0,0.3);
    white-space: nowrap;
  }
  .label-salsa { top: 496px; }
  .label-bachata { top: 591px; }
  .label-kizomba { top: 684px; }
</style>
</head>
<body>
<main class="member-card">
  <span class="brand-name">SOLARA</span>
  <span class="brand-sub">DANCE STUDIO</span>

  <h1 class="card-title">LID KAART</h1>

  <p class="field field-name">NAAM:.....................</p>
  <p class="field field-styles">DANSSTIJLEN:..............</p>

  <div class="dancers-photo" role="img" aria-label="Photo of a couple dancing tango, woman in black dress and man in dark suit"></div>

  <svg class="stamp-grid" width="1200" height="853" viewBox="0 0 1200 853" aria-hidden="true">
    <defs>
      <ellipse id="stamp" cx="0" cy="0" rx="34" ry="39" stroke="var(--dot-stroke)" stroke-width="1"/>
    </defs>
    <g class="row-salsa" fill="var(--salsa)">
      <use href="#stamp" x="102" y="527"/><use href="#stamp" x="177" y="527"/><use href="#stamp" x="252" y="527"/><use href="#stamp" x="327" y="527"/>
      <use href="#stamp" x="402" y="527"/><use href="#stamp" x="476" y="527"/><use href="#stamp" x="551" y="527"/><use href="#stamp" x="626" y="527"/>
      <use href="#stamp" x="701" y="527"/><use href="#stamp" x="776" y="527"/><use href="#stamp" x="850" y="527"/><use href="#stamp" x="925" y="527"/>
    </g>
    <g class="row-bachata" fill="var(--bachata)">
      <use href="#stamp" x="102" y="617"/><use href="#stamp" x="177" y="617"/><use href="#stamp" x="252" y="617"/><use href="#stamp" x="327" y="617"/>
      <use href="#stamp" x="402" y="617"/><use href="#stamp" x="476" y="617"/><use href="#stamp" x="551" y="617"/><use href="#stamp" x="626" y="617"/>
      <use href="#stamp" x="701" y="617"/><use href="#stamp" x="776" y="617"/><use href="#stamp" x="850" y="617"/><use href="#stamp" x="925" y="617"/>
    </g>
    <g class="row-kizomba" fill="var(--kizomba)">
      <use href="#stamp" x="102" y="702"/><use href="#stamp" x="177" y="702"/><use href="#stamp" x="252" y="702"/><use href="#stamp" x="327" y="702"/>
      <use href="#stamp" x="402" y="702"/><use href="#stamp" x="476" y="702"/><use href="#stamp" x="551" y="702"/><use href="#stamp" x="626" y="702"/>
      <use href="#stamp" x="701" y="702"/><use href="#stamp" x="776" y="702"/><use href="#stamp" x="850" y="702"/><use href="#stamp" x="925" y="702"/>
    </g>
  </svg>

  <span class="style-label label-salsa">SALSA</span>
  <span class="style-label label-bachata">BACHATA</span>
  <span class="style-label label-kizomba">KIZOMBA</span>
</main>
</body>
</html>
```